Acupuncture Medspa needs a business card design

I need a business card design that looks professional, has a spa-like quality and can offer a promo on the back. Initial promo is "First session free". The tagline of NeedleNook is: Refresh, Restore, Rejuvenate.

NeedleNook is a membership-based acupuncture medspa that offers acupuncture, cupping, and herbal therapies. Members choose between the "Refresh" membership which is for stress relief, or "Restore" which is for treating health conditions, and lastly "Rejuvenate" which is for natural facial enhancement.

Industry/Entity Type

Health And Wellness

Contact Information for Business Card

Coral Haskins, MAC, L.Ac.
612-555-0193
www.needlenook-example.com

Font styles to use
Serif
Sans Serif

Colors

Designer to choose colors to be used in the design.

Requirements
Must have
• The project must have NeedleNook logo, promo on the back, and contact information
Nice to have
• I would like to see the colors of the logo used.

```html
<!DOCTYPE html>
<html lang="en">
<head>
<meta charset="utf-8">
<title>NeedleNook Business Card</title>
<link href="https://fonts.googleapis.com/css2?family=Montserrat:wght@400;500;600&display=swap" rel="stylesheet">
<style>
  :root {
    --teal: #1a8a80;
    --teal-soft: #cfe3e2;
    --charcoal: #262626;
    --pattern: #2f2f2f;
    --ink: #2b2b2b;
    --paper: #ffffff;
    --paper-shade: #eeeeee;
    --stage: #d9d9d9;
    --white: #ffffff;
  }
  * { margin: 0; padding: 0; box-sizing: border-box; }
  html, body { width: 1200px; height: 1021px; overflow: hidden; }
  body {
    background: var(--stage);
    font-family: "Montserrat", sans-serif;
    position: relative;
  }
  .card {
    position: absolute;
    left: 210px;
    width: 780px;
    height: 446px;
    overflow: hidden;
    box-shadow: 0 8px 22px rgba(0,0,0,0.25);
  }
  /* Back side */
  .card-back { top: 44px; background: var(--charcoal); }
  .back-pattern {
    position: absolute; inset: 0;
    background: var(--pattern);
    opacity: 0.55;
  }
  .back-content {
    position: absolute; inset: 0;
    display: flex; flex-direction: column; align-items: center; justify-content: center;
  }
  .brand-name {
    color: var(--teal);
    font-weight: 500;
    letter-spacing: 0.02em;
    display: flex; align-items: center; gap: 14px;
  }
  .brand-mark {
    border: 4px solid var(--teal);
    border-radius: 50%;
  }
  .card-back .brand-name { font-size: 64px; }
  .card-back .brand-mark { width: 60px; height: 60px; }
  .tagline {
    color: var(--white);
    font-size: 22px;
    letter-spacing: 0.2em;
    margin-top: 14px;
  }
  .promo {
    color: var(--teal);
    font-size: 24px;
    font-weight: 600;
    letter-spacing: 0.06em;
    margin-top: 34px;
  }
  /* Front side */
  .card-front {
    top: 530px;
    background: linear-gradient(120deg, var(--paper) 40%, var(--paper-shade) 100%);
  }
  .card-front .brand-name {
    position: absolute; left: 52px; top: 48px;
    font-size: 46px;
  }
  .card-front .brand-mark { width: 44px; height: 44px; border-width: 3px; }
  .faint-circle {
    position: absolute; right: -20px; top: 90px;
    width: 360px; height: 360px;
    border: 5px solid var(--teal-soft);
    border-radius: 50%;
  }
  .contact-list {
    position: absolute; left: 52px; top: 198px;
    list-style: none;
    font-size: 19px;
    color: var(--ink);
  }
  .contact-list li { display: flex; align-items: center; gap: 10px; margin-bottom: 6px; }
  .contact-list svg { width: 16px; height: 16px; fill: none; stroke: var(--teal); stroke-width: 2; }
  .holder {
    position: absolute; left: 420px; top: 250px;
    color: var(--teal);
    font-size: 26px; font-weight: 600;
    letter-spacing: 0.02em;
  }
  .holder .credentials { font-size: 18px; font-weight: 500; }
  .wave { position: absolute; left: 0; bottom: 0; width: 780px; height: 190px; }
</style>
</head>
<body>

<section class="card card-back">
  <div class="back-pattern" role="img" aria-label="Repeating pattern of small brand emblems in dark grey"></div>
  <div class="back-content">
    <div class="brand-name"><span class="brand-mark"></span>NeedleNook</div>
    <p class="tagline">Refresh · Restore · Rejuvenate</p>
    <p class="promo">FIRST SESSION FREE</p>
  </div>
</section>

<section class="card card-front">
  <div class="faint-circle"></div>
  <div class="brand-name"><span class="brand-mark"></span>NeedleNook</div>

  <ul class="contact-list">
    <li>
      <svg viewBox="0 0 16 16"><path d="M3 1.5l3 .5 1 3-2 1.5a9 9 0 0 0 4.5 4.5L11 9l3 1 .5 3c-1 1.5-3 2-5 1A13 13 0 0 1 2 6.5c-1-2-.5-4 1-5z" fill="var(--teal)" stroke="none"/></svg>
      612-555-0193
    </li>
    <li>
      <svg viewBox="0 0 16 16"><rect x="1.5" y="3.5" width="13" height="9"/><path d="M1.5 3.5l6.5 5 6.5-5"/></svg>
      coral@needlenook-example.com
    </li>
    <li>
      <svg viewBox="0 0 16 16"><circle cx="8" cy="8" r="6.5"/><path d="M1.5 8h13M8 1.5c-3 3.5-3 9.5 0 13M8 1.5c3 3.5 3 9.5 0 13"/></svg>
      www.needlenook-example.com
    </li>
  </ul>

  <p class="holder">CORAL HASKINS, <span class="credentials">MAC, L.Ac.</span></p>

  <svg class="wave" viewBox="0 0 780 190" preserveAspectRatio="none">
    <path d="M0 40 C 180 110, 420 150, 560 150 C 560 150, 300 120, 0 30 Z" fill="var(--ink)"/>
    <path d="M0 52 C 200 130, 420 170, 560 160 C 660 152, 730 120, 780 96 L780 190 L0 190 Z" fill="var(--teal)"/>
  </svg>
</section>

</body>
</html>
```